Design a web site for my business - Brellan Coatworks Mackaby.

We are a family business that handles design, fabrication and installation of powder coated aluminum, stainless steel and glass products. Including handrails, privacy slat screens, electric gates and pool fencing. We are based in the Whitsundays in North Queensland and service an area from Airlie Beach to Townsville.

Target Market(s)

Domestic and commercial

Industry/Entity Type

fabrication - manufacturing

Coding

Coded - Design and coding required

Number of Pages Required

5+ page

Colors
0054AA
0677BA
7BADD7
CADEEF
E8F1F8

Requirements
Must have
• photo galleries, contact page, one page for privacy screens, balustrades, glass fencing, stainless steel handrail, powder coated aluminium handrails and pool fencing

```html
<!DOCTYPE html>
<html lang="en">
<head>
<meta charset="utf-8">
<title>Brellan Coatworks Mackaby — Services</title>
<link rel="stylesheet" href="https://fonts.googleapis.com/css2?family=Inter:wght@400;500;600;700;800&display=swap">
<style>
:root{
  --blue:#0054AA;
  --blue-mid:#0677BA;
  --blue-soft:#7BADD7;
  --blue-pale:#CADEEF;
  --blue-wash:#E8F1F8;
  --blue-deep:#003A78;
  --heading:#0c2c52;
  --paper:#f8fbfd;
  --line:#CADEEF;
  --text:#1a2636;
  --muted:#56657a;
  --white:#ffffff;
}
*{box-sizing:border-box;margin:0;padding:0}
html,body{width:1200px;height:3167px;overflow:hidden}
body{font-family:"Inter",sans-serif;background:var(--paper);color:var(--text);position:relative}
.abs{position:absolute}
a{color:inherit;text-decoration:none}

/* header */
.site-header{position:absolute;left:0;top:0;width:1200px;height:76px;border-bottom:1px solid var(--line);background:var(--white)}
.brand{position:absolute;left:62px;top:22px;display:flex;align-items:center;gap:8px;font-size:12px;font-weight:700;line-height:1.25;color:var(--heading);width:150px}
.brand-mark{width:14px;height:14px;background:var(--blue);flex:none}
.main-nav{position:absolute;left:373px;top:26px;display:flex;gap:30px;font-size:15px;color:var(--muted)}
.main-nav .active{color:var(--blue);font-weight:600;border-bottom:2px solid var(--blue);padding-bottom:6px}
.btn{display:flex;align-items:center;justify-content:center;font-weight:600;font-size:15px}
.btn-dark{background:var(--blue);color:var(--white)}
.btn-outline{border:1px solid var(--blue-soft);color:var(--blue);background:var(--white)}
.header-cta{left:986px;top:16px;width:152px;height:43px;border-radius:3px}

/* hero */
.hero{position:absolute;left:0;top:76px;width:1200px;height:573px;border-bottom:1px solid var(--line);background:var(--blue-wash)}
.eyebrow{left:62px;top:120px;background:var(--blue);color:var(--white);font-size:11px;font-weight:700;letter-spacing:.5px;padding:5px 11px}
.hero h1{left:62px;top:162px;font-size:47px;font-weight:700;line-height:1.1;letter-spacing:-.5px;color:var(--heading)}
.hero p{left:62px;top:292px;width:480px;font-size:17px;line-height:26px;color:var(--muted)}
.hero .b1{left:62px;top:400px;width:187px;height:54px}
.hero .b2{left:265px;top:400px;width:152px;height:54px}
.hero-pill{left:587px;top:280px;width:26px;height:11px;border-radius:6px;background:var(--blue-soft)}
.hero-photo{left:623px;top:99px;width:515px;height:374px;background:linear-gradient(135deg,#6da2bd 0%,#3f7590 45%,#5c6a6d 75%,#a79f93 100%);box-shadow:0 10px 24px rgba(0,58,120,.15)}

/* services */
.card{position:absolute;border:1px solid var(--line);border-radius:4px;background:var(--white);overflow:hidden}
.card h2{font-size:29px;font-weight:700;line-height:1.25;letter-spacing:-.3px;color:var(--heading)}
.card p{font-size:15px;line-height:22px;color:var(--muted)}
.photo{position:absolute}
.tag-row{display:flex;flex-wrap:wrap;gap:12px 12px;width:200px}
.tag{display:flex;align-items:center;gap:5px;background:var(--blue-wash);border-radius:14px;padding:4px 11px;font-size:13px;color:var(--text)}
.tag svg{width:14px;height:14px}
.link-arrow{display:flex;align-items:center;gap:8px;font-size:15px;font-weight:600;color:var(--blue)}
.link-arrow.underlined{border-bottom:2px solid var(--blue);padding-bottom:2px}
.card-dark{background:var(--blue);border-color:var(--blue)}
.card-dark h2{color:var(--white);font-size:23px}
.card-dark p{color:var(--blue-pale)}
.check-list{list-style:none;display:flex;flex-direction:column;gap:14px;font-size:15px}
.check-list li{display:flex;align-items:center;gap:9px}
.feature-box{background:var(--blue-wash);padding:16px 15px;width:225px;height:70px}
.feature-box strong{display:block;font-size:15px;color:var(--heading)}
.feature-box span{font-size:13px;color:var(--muted)}

/* method */
.method{position:absolute;left:0;top:1902px;width:1200px;height:551px;border-top:1px solid var(--line);border-bottom:1px solid var(--line);background:var(--white)}
.method .label{left:0;width:1200px;top:115px;text-align:center;font-size:11px;font-weight:600;letter-spacing:1.5px;color:var(--blue-mid)}
.method h2{left:0;width:1200px;top:142px;text-align:center;font-size:46px;font-weight:700;letter-spacing:-.6px;color:var(--heading)}
.method-line{left:62px;top:299px;width:1076px;height:2px;background:var(--blue-pale)}
.step{position:absolute;top:258px;width:260px;text-align:center}
.step-icon{width:82px;height:83px;margin:0 auto;background:var(--blue);border-radius:4px;display:flex;align-items:center;justify-content:center;box-shadow:0 6px 14px rgba(0,84,170,.2)}
.step h3{margin-top:24px;font-size:22px;font-weight:600;color:var(--heading)}
.step p{margin-top:10px;font-size:13px;line-height:18px;color:var(--muted)}

/* cta */
.cta{position:absolute;left:62px;top:2528px;width:1076px;height:195px;background:var(--blue);border-radius:10px;color:var(--white)}
.cta h2{left:45px;top:48px;font-size:30px;font-weight:700;letter-spacing:-.3px}
.cta p{left:45px;top:100px;width:480px;font-size:17px;line-height:26px;color:var(--blue-wash)}
.cta .dash{left:527px;top:96px;width:22px;height:3px;background:var(--blue-mid)}
.cta .c1{left:640px;top:65px;width:209px;height:66px;background:var(--white);color:var(--blue);border-radius:3px;font-size:16px}
.cta .c2{left:865px;top:65px;width:166px;height:66px;border:1px solid var(--blue-soft);border-radius:3px;color:var(--white);font-size:16px}

/* footer */
.site-footer{position:absolute;left:0;top:2798px;width:1200px;height:369px;background:var(--blue-deep);color:var(--white)}
.footer-brand{left:62px;top:36px;display:flex;align-items:center;gap:8px;font-size:13px;font-weight:700;width:160px;line-height:1.25}
.footer-brand .brand-mark{background:var(--white)}
.footer-tag{left:62px;top:122px;width:240px;font-size:15px;line-height:22px;color:var(--blue-pale)}
.social{top:197px;width:38px;height:38px;border:1.5px solid var(--white);border-radius:8px;display:flex;align-items:center;justify-content:center}
.footer-col{top:57px}
.footer-col h4{font-size:15px;font-weight:600;margin-bottom:22px}
.footer-col ul{list-style:none;display:flex;flex-direction:column;gap:16px;font-size:15px;color:var(--blue-soft)}
.legal{left:62px;top:310px;font-size:12px;color:var(--blue-pale)}
.legal-links{right:62px;top:310px;display:flex;gap:24px;font-size:12px;color:var(--blue-pale)}
</style>
</head>
<body>

<header class="site-header">
  <a class="brand" href="#"><span class="brand-mark"></span>Brellan Coatworks<br>Mackaby</a>
  <nav class="main-nav">
    <a class="active" href="#">Services</a>
    <a href="#">Projects</a>
    <a href="#">Areas</a>
    <a href="#">About</a>
    <a href="#">Contact</a>
  </nav>
  <a class="btn btn-dark abs header-cta" href="#">Request Quote</a>
</header>

<section class="hero">
  <span class="abs eyebrow">PREMIUM CRAFTSMANSHIP</span>
  <h1 class="abs">Expert Fabrication<br>Services</h1>
  <p class="abs">Precision-engineered aluminum and steel solutions for high-end coastal properties. We balance industrial strength with architectural elegance.</p>
  <a class="btn btn-dark abs b1" href="#">Explore Solutions</a>
  <a class="btn btn-outline abs b2" href="#">View Gallery</a>
  <span class="abs hero-pill"></span>
  <div class="abs hero-photo" role="img" aria-label="Stainless steel and glass balustrade on a terrace overlooking a blue bay and islands"></div>
</section>

<article class="card" style="left:62px;top:740px;width:710px;height:512px">
  <h2 class="abs" style="left:30px;top:30px">Handrails &amp;<br>Balustrades</h2>
  <p class="abs" style="left:30px;top:121px;width:300px">Combining marine-grade stainless steel with architectural glass for safety that doesn't compromise your view.</p>
  <div class="abs tag-row" style="left:30px;top:210px">
    <span class="tag"><svg viewBox="0 0 16 16" fill="none" stroke="#0054AA" stroke-width="1.5"><circle cx="8" cy="8" r="6"/><path d="M5.5 8l1.8 1.8L10.5 6.5"/></svg>Durability</span>
    <span class="tag"><svg viewBox="0 0 16 16" fill="none" stroke="#0054AA" stroke-width="1.4"><path d="M7 2l1.3 3.7L12 7l-3.7 1.3L7 12 5.7 8.3 2 7l3.7-1.3z"/><path d="M12.5 10.5v3M11 12h3"/></svg>Style</span>
    <span class="tag"><svg viewBox="0 0 16 16" fill="none" stroke="#0054AA" stroke-width="1.4"><path d="M6 2h4v5H6zM3 7h10v3H3zM4 10v4M8 10v4M12 10v4"/></svg>Low Maintenance</span>
  </div>
  <a class="abs link-arrow underlined" style="left:30px;top:312px" href="#">View Project Gallery
    <svg width="16" height="16" viewBox="0 0 16 16" fill="none" stroke="#0054AA" stroke-width="1.8"><path d="M2 8h11M9 4l4 4-4 4"/></svg></a>
  <div class="photo" role="img" aria-label="Timber boardwalk with stainless steel wire balustrade among coastal bushland" style="left:369px;top:30px;width:310px;height:301px;background:linear-gradient(160deg,#4f5e44 0%,#6f7258 40%,#8a6d56 70%,#9b9585 100%)"></div>
</article>

<article class="card card-dark" style="left:795px;top:740px;width:343px;height:512px">
  <div class="photo" role="img" aria-label="Cream powder-coated aluminium slat screens and gate beside a house" style="left:0;top:0;width:343px;height:179px;background:linear-gradient(180deg,#5a7a9a 0%,#9aa7ad 45%,#d9d3c5 100%)"></div>
  <h2 class="abs" style="left:30px;top:210px">Privacy Slat Screens</h2>
  <p class="abs" style="left:30px;top:254px;width:290px">Powder-coated aluminum solutions designed for optimal airflow and visual seclusion.</p>
  <ul class="abs check-list" style="left:30px;top:344px;color:var(--white)">
    <li><svg width="18" height="18" viewBox="0 0 18 18" fill="none" stroke="#fff" stroke-width="1.5"><circle cx="9" cy="9" r="7.5"/><path d="M5.8 9.2l2.2 2.2 4.3-4.5"/></svg>Weather Resistant</li>
    <li><svg width="18" height="18" viewBox="0 0 18 18" fill="none" stroke="#fff" stroke-width="1.5"><circle cx="9" cy="9" r="7.5"/><path d="M5.8 9.2l2.2 2.2 4.3-4.5"/></svg>Custom Color Match</li>
  </ul>
  <a class="btn abs" style="left:30px;top:430px;width:284px;height:53px;background:var(--white);color:var(--blue)" href="#">View Gallery</a>
</article>

<article class="card" style="left:62px;top:1275px;width:526px;height:550px">
  <div class="photo" role="img" aria-label="Modern home with sandstone walls and a dark horizontal slat driveway gate" style="left:0;top:0;width:526px;height:240px;background:linear-gradient(180deg,#a9c2d3 0%,#b2a48c 40%,#6e6a5c 70%,#8d8d88 100%)"></div>
  <h2 class="abs" style="left:30px;top:269px">Electric &amp; Manual Gates</h2>
  <p class="abs" style="left:30px;top:314px;width:470px">Sophisticated entry systems featuring high-torque automation for effortless security.</p>
  <div class="abs feature-box" style="left:30px;top:382px"><strong>Durability</strong><span>Industrial Grade</span></div>
  <div class="abs feature-box" style="left:270px;top:382px"><strong>Security</strong><span>Smart Access</span></div>
  <a class="btn btn-dark abs" style="left:30px;top:475px;width:466px;height:45px" href="#">View Project Gallery</a>
</article>

<article class="card" style="left:612px;top:1275px;width:526px;height:550px">
  <h2 class="abs" style="left:30px;top:130px">Pool Fencing</h2>
  <p class="abs" style="left:30px;top:182px;width:205px">Compliant, crystal-clear glass or aluminum tube fencing that protects your family while enhancing the poolside aesthetic.</p>
  <ul class="abs check-list" style="left:30px;top:318px;gap:12px;color:var(--text)">
    <li><svg width="17" height="17" viewBox="0 0 18 18" fill="none" stroke="#0054AA" stroke-width="1.6"><path d="M9 1.8l6 2.4v4.3c0 3.7-2.6 6.4-6 7.7-3.4-1.3-6-4-6-7.7V4.2z"/></svg>Safety Standard Certified</li>
    <li><svg width="18" height="18" viewBox="0 0 18 18" fill="none" stroke="#0054AA" stroke-width="1.5"><path d="M9 1.8a7.2 7.2 0 100 14.4c1.2 0 1.6-1 1-1.9-.6-1 .1-2.1 1.2-2.1h1.8a3.2 3.2 0 003.2-3.2A7.2 7.2 0 009 1.8z"/><circle cx="5.5" cy="8.5" r="1"/><circle cx="8" cy="5.5" r="1"/><circle cx="11.5" cy="6" r="1"/></svg>Custom Powder Coating</li>
  </ul>
  <a class="abs link-arrow" style="left:30px;top:400px" href="#">View Gallery
    <svg width="16" height="16" viewBox="0 0 16 16" fill="none" stroke="#0054AA" stroke-width="1.8"><path d="M2 8h11M9 4l4 4-4 4"/></svg></a>
  <div class="photo" role="img" aria-label="Frameless glass pool fence beside tropical plants and stone paving" style="left:263px;top:0;width:263px;height:550px;background:linear-gradient(180deg,#506a48 0%,#3f5a3c 35%,#7f8a7c 65%,#8e8c86 100%)"></div>
</article>

<section class="method">
  <span class="abs label">OUR METHODOLOGY</span>
  <h2 class="abs">Precision From Start to Finish</h2>
  <span class="abs method-line"></span>
  <div class="step" style="left:57px">
    <div class="step-icon"><svg width="34" height="34" viewBox="0 0 24 24" fill="none" stroke="#fff" stroke-width="1.8" stroke-linejoin="round"><path d="M12 3l9 9-9 9-9-9z"/><path d="M8 12.5l2.5-2.5 2 2 3-3"/></svg></div>
    <h3>Consultation</h3>
    <p>On-site measurement and requirements analysis for your specific coastal environment.</p>
  </div>
  <div class="step" style="left:333px">
    <div class="step-icon"><svg width="30" height="30" viewBox="0 0 24 24" fill="none" stroke="#fff" stroke-width="1.8" stroke-linecap="round"><circle cx="12" cy="5" r="2"/><path d="M11 7l-5 14M13 7l5 14M8.5 15h7"/></svg></div>
    <h3>Design</h3>
    <p>Detailed 3D modelling and material selection to ensure architectural harmony.</p>
  </div>
  <div class="step" style="left:607px">
    <div class="step-icon"><svg width="32" height="32" viewBox="0 0 24 24" fill="none" stroke="#fff" stroke-width="1.8" stroke-linecap="round"><path d="M5 21h9M8 21v-6l-3-4 4-3 4 4h5"/><circle cx="18" cy="9" r="2.5"/></svg></div>
    <h3>Fabrication</h3>
    <p>Workshop crafting using high-grade materials and precision welding techniques.</p>
  </div>
  <div class="step" style="left:883px">
    <div class="step-icon"><svg width="32" height="32" viewBox="0 0 24 24" fill="none" stroke="#fff" stroke-width="2" stroke-linecap="round"><path d="M4 20l9-9M14 4a4 4 0 005 5l-3 3-5-5zM6 4l3 3-2 2-3-3zM13 13l7 7"/></svg></div>
    <h3>Installation</h3>
    <p>Expert on-site fitting with attention to structural integrity and finishing details.</p>
  </div>
</section>

<section class="cta">
  <h2 class="abs">Ready to elevate your property?</h2>
  <p class="abs">Contact us for a free on-site consultation and quote in the Whitsunday region.</p>
  <span class="abs dash"></span>
  <a class="btn abs c1" href="#">Request a Quote</a>
  <a class="btn abs c2" href="#">Contact Us</a>
</section>

<footer class="site-footer">
  <a class="abs footer-brand" href="#"><span class="brand-mark"></span>Brellan Coatworks<br>Mackaby</a>
  <p class="abs footer-tag">Precision Craftsmanship for the Coast.</p>
  <a class="abs social" style="left:62px" href="#" aria-label="Website"><svg width="20" height="20" viewBox="0 0 24 24" fill="none" stroke="#fff" stroke-width="1.8"><circle cx="12" cy="12" r="9"/><path d="M3 12h18M12 3c3 3 3 15 0 18M12 3c-3 3-3 15 0 18"/></svg></a>
  <a class="abs social" style="left:114px" href="#" aria-label="Email"><svg width="20" height="20" viewBox="0 0 24 24" fill="none" stroke="#fff" stroke-width="1.8"><rect x="3" y="5" width="18" height="14" rx="2"/><path d="M3 7l9 6 9-6"/></svg></a>
  <div class="abs footer-col" style="left:337px"><h4>Our Services</h4><ul><li>Handrails</li><li>Privacy Screens</li><li>Electric Gates</li><li>Pool Fencing</li></ul></div>
  <div class="abs footer-col" style="left:612px"><h4>More</h4><ul><li>Glass Balustrades</li><li>Custom Fabrication</li></ul></div>
  <div class="abs footer-col" style="left:886px"><h4>Service Areas</h4><ul><li>Airlie Beach</li><li>Bowen</li><li>Townsville</li></ul></div>
  <p class="abs legal">© 2024 Mackaby Fabrication Co. Precision Craftsmanship for the Coast.</p>
  <div class="abs legal-links"><a href="#">Privacy Policy</a><a href="#">Terms of Service</a></div>
</footer>

</body>
</html>
```